Wordpress Theme for a Professional Speaker's Website

I I need a website to promote myself as a speaker to corporations and meeting planners. Some examples of similar sites I like are:

http://www.beginwithpurpose-demo.net (this is by far my favorite)
http://www.lorapemberton.net
http://www.teddyvance.net
http://www.bolsinter.net
http://www.dawnacrossridges.net
http://www.rudyfallenbrook.net

I like modern, minimalistic, innovative. I'm okay if it's edgy but still want it communicate professionalism.

The primary objective is to position me as an expert who can deliver valuable information in an entertaining manner.

There are two calls to action. The first is to capture name and email address to subscribe to my newsletter. The second is to request more information about booking me to speak for their company, organization, etc.

The pages on the website will ultimately be the following:

1. Home (should include sections for recent blog posts, featured topics/presentations, short bio, testimonials, email capture, and anything else you think should be added.
2. Meet Owen
3. Blog
4. Keynotes & Speaking
5. Training & Webinars
6. Coaching & Consulting
7. Testimonials
8. Book Owen
9. Media Inquiries
10. Contact

Please feel free to use your creativity. I don't want my requirements to limit you in any way. I'm just looking for a modern, professional site that will make me stand out from the crowd.

I don't have any existing site or brand identity. My plan is to have the website design I ultimately choose serve as the foundation for the rest of my brand identity.

Target Market(s)

Corporate meeting planners and executives

Industry/Entity Type

It Professional

Font styles to use
Sans Serif

Requirements
Must have
• Email capture, testimonials, blog
Nice to have
• None
Should not have
• None

```html
<!DOCTYPE html>
<html lang="en">
<head>
<meta charset="utf-8">
<title>Blog – Owen Halvorsen</title>
<link rel="stylesheet" href="https://fonts.googleapis.com/css2?family=Share+Tech+Mono&family=Arimo:wght@400&display=swap">
<style>
:root{
  --navy:#02496b;
  --ink:#0d4a6b;
  --page:#e4e4e4;
  --footer:#959595;
  --body:#767676;
  --meta:#ababab;
  --rule:#7a7a7a;
  --frame:#bdbdbd;
  --accent:#c0391b;
  --white:#ffffff;
  --mono:'Share Tech Mono', monospace;
  --sans:'Arimo', Arial, sans-serif;
}
*{margin:0;padding:0;box-sizing:border-box}
html,body{width:1029px;height:1200px;overflow:hidden;background:var(--page)}
.site{position:relative;width:1029px;height:1200px;background:var(--page);font-family:var(--sans)}
.abs{position:absolute}
.site-header{position:absolute;left:0;top:0;width:1029px;height:58px;background:var(--navy)}
.brand{left:49px;top:19px;font-family:var(--mono);color:var(--white);font-size:17px;letter-spacing:2.6px;line-height:18px;white-space:nowrap}
.main-nav a{position:absolute;top:21px;font-family:var(--mono);color:var(--white);font-size:13px;letter-spacing:2px;text-decoration:none;line-height:14px;white-space:nowrap}
.main-nav .current{border-bottom:2px solid var(--white);padding:0 9px 3px;margin-left:-9px}
.page-title{left:0;top:88px;width:672px;height:38px}
.page-title .rule{position:absolute;top:17px;height:3px;background:var(--rule)}
.page-title h1{position:absolute;left:176px;top:0;font-family:var(--mono);font-weight:400;font-size:31px;letter-spacing:5px;color:var(--rule);line-height:38px}
.thumb{background:var(--frame);padding:6px}
.thumb div{width:100%;height:100%}
.post-title{font-weight:400;font-size:17.5px;color:var(--ink);line-height:20px;white-space:nowrap}
.post-meta{font-size:12px;color:var(--meta);line-height:14px;white-space:nowrap}
.post-text{font-size:15.2px;line-height:18.5px;color:var(--body);white-space:nowrap}
.post-text p.gap{margin-top:18.5px}
.search-label{left:715px;top:116px;font-size:17px;color:#b5b5b5;line-height:20px}
.search-box{left:715px;top:142px;width:258px;height:27px;background:var(--white);border:2px solid #c3c3c3}
.newsletter{left:743px;top:249px;width:202px;height:182px;background:var(--navy)}
.newsletter .mark{position:absolute;left:52px;top:0;width:104px;height:58px;background:linear-gradient(135deg,#e9eef2,#c9d6df 60%,#b8533a)}
.newsletter .field{position:absolute;left:24px;top:83px;width:153px;height:27px;background:var(--white)}
.newsletter .submit{position:absolute;left:51px;top:129px;width:100px;height:24px;background:var(--accent);color:var(--white);font-family:var(--mono);font-size:12px;letter-spacing:2.5px;text-align:center;line-height:24px}
.recent h2{font-family:var(--mono);font-weight:400;font-variant:small-caps;font-size:22px;letter-spacing:3px;color:var(--ink);line-height:24px;white-space:nowrap}
.recent li{list-style:none;font-size:15px;line-height:18.5px;color:var(--body)}
.site-footer{position:absolute;left:0;top:935px;width:1029px;height:265px;background:var(--footer)}
.foot-head{font-family:var(--mono);font-weight:400;font-size:19px;letter-spacing:3.5px;color:var(--ink);line-height:22px;white-space:nowrap}
.foot-menu li{list-style:none;font-size:14px;line-height:16.6px;color:#555}
.social span{position:absolute;top:110px;width:11px;height:11px;border-radius:50%;background:var(--ink)}
.contact-info{font-size:12px;line-height:14.4px;color:var(--ink);text-align:center}
</style>
</head>
<body>
<div class="site">
  <header class="site-header">
    <div class="abs brand">OWEN HALVORSEN</div>
    <nav class="main-nav">
      <a style="left:490px">HOME</a>
      <a style="left:550px">MEET OWEN</a>
      <a style="left:658px">KEYNOTE &amp; SPEAKING</a>
      <a class="current" style="left:843px">BLOG</a>
      <a style="left:900px">CONTACT</a>
    </nav>
  </header>

  <div class="abs page-title">
    <span class="rule" style="left:0;width:161px"></span>
    <h1>BLOG</h1>
    <span class="rule" style="left:305px;width:367px"></span>
  </div>

  <article>
    <div class="abs thumb" style="left:62px;top:163px;width:167px;height:143px">
      <div role="img" aria-label="Road sign pointing towards success under a bright cloudy sky" style="background:linear-gradient(160deg,#5f88b8,#cfd9e6 55%,#4e7a3c)"></div>
    </div>
    <h2 class="abs post-title" style="left:259px;top:160px">BLOG CONTENT 1</h2>
    <div class="abs post-meta" style="left:259px;top:188px">Jan 1 2016 | By Admin | Posted in Category</div>
    <div class="abs post-text" style="left:252px;top:218px">
      <p>Lorem ipsum dolor sit amet, consectetur adipiscing elit, sed<br>do eiusmod tempor incididunt ut labore et dolore magna ali<br>qua. Ut enim ad minim veniam, quis nostrud exercitation ull<br>amco laboris nisi ut aliquip ex ea commodo consequat. Dui<br>s aute irure dolor.</p>
    </div>
    <div class="abs post-text" style="left:61px;top:321px">
      <p>Lorem ipsum dolor sit amet, consectetur adipiscing elit, seddo eiusmod tempor&nbsp; incididu<br>nt ut labore et dolore magna aliqua. Ut enim ad minim veniam, quis nostrud&nbsp; exercitation<br>ullamco laboris nisi ut aliquip ex ea commodo consequat. Dui s aute irure dolor i</p>
      <p class="gap">Lorem ipsum dolor sit amet, consectetur adipiscing elit, seddo eiusmod tempor&nbsp; incididu<br>nt ut labore et dolore magna aliqua. Ut enim ad minim veniam, quis nostrud&nbsp; exercitation<br>ullamco laboris nisi ut aliquip ex ea commodo consequat. Dui s aute irure dolor i</p>
      <p>Lorem ipsum dolor sit amet, consectetur adipiscing elit, seddo eiusmod tempor&nbsp; incididu<br>nt ut labore et dolore magna aliqua. Ut enim ad minim veniam, quis nostrud&nbsp; exercitation<br>ullamco laboris nisi ut aliquip ex ea commodo consequat. Dui s aute irure dolor i</p>
    </div>
  </article>

  <article>
    <div class="abs thumb" style="left:57px;top:560px;width:168px;height:143px">
      <div role="img" aria-label="Red darts hitting the centre of a green target" style="background:linear-gradient(90deg,#ffffff 20%,#e4e4e4 45%,#62c64d 70%,#2a3a2a)"></div>
    </div>
    <h2 class="abs post-title" style="left:255px;top:557px">BLOG CONTENT 2</h2>
    <div class="abs post-meta" style="left:255px;top:585px">Jan 1 2016 | By Admin | Posted in Category</div>
    <div class="abs post-text" style="left:248px;top:615px">
      <p>Lorem ipsum dolor sit amet, consectetur adipiscing elit, sed<br>do eiusmod tempor incididunt ut labore et dolore magna ali<br>qua. Ut enim ad minim veniam, quis nostrud exercitation ull<br>amco laboris nisi ut aliquip ex ea commodo consequat. Dui<br>s aute irure dolor.</p>
    </div>
    <div class="abs post-text" style="left:57px;top:718px">
      <p>Lorem ipsum dolor sit amet, consectetur adipiscing elit, seddo eiusmod tempor&nbsp; incididu<br>nt ut labore et dolore magna aliqua. Ut enim ad minim veniam, quis nostrud&nbsp; exercitation<br>ullamco laboris nisi ut aliquip ex ea commodo consequat. Dui s aute irure dolor i</p>
      <p class="gap">Lorem ipsum dolor sit amet, consectetur adipiscing elit, seddo eiusmod tempor&nbsp; incididu<br>nt ut labore et dolore magna aliqua. Ut enim ad minim veniam, quis nostrud&nbsp; exercitation<br>ullamco laboris nisi ut aliquip ex ea commodo consequat. Dui s aute irure dolor i</p>
      <p>Lorem ipsum dolor sit amet, consectetur adipiscing elit, seddo eiusmod tempor&nbsp; incididu<br>nt ut labore et dolore magna aliqua. Ut enim ad minim veniam, quis nostrud&nbsp; exercitation<br>ullamco laboris nisi ut aliquip ex ea commodo consequat. Dui s aute irure dolor i</p>
    </div>
  </article>

  <aside>
    <div class="abs search-label">search</div>
    <div class="abs search-box"></div>

    <div class="abs newsletter">
      <div class="mark" role="img" aria-label="Hand-drawn envelope illustration with a checkmark"></div>
      <div class="field"></div>
      <div class="submit">SUBMIT</div>
    </div>

    <div class="abs recent" style="left:791px;top:462px">
      <h2>Recent Posts</h2>
      <ul style="margin-top:21px">
        <li>Blog Content 1</li>
        <li>Blog Content 2</li>
        <li>Blog Content 3</li>
        <li>Blog Content 4</li>
        <li>Blog Content 5</li>
      </ul>
    </div>

    <div class="abs" role="img" aria-label="Photo of the speaker seated, gesturing with both hands" style="left:740px;top:660px;width:263px;height:275px;background:linear-gradient(180deg,rgba(228,228,228,0) 0%,#e7b7ad 25%,#d98f86 55%,#4d6384 85%,#3c4f6e);border-radius:120px 120px 0 0"></div>
  </aside>

  <footer class="site-footer">
    <div class="abs" style="left:91px;top:78px">
      <h3 class="foot-head">MENU 1</h3>
      <ul class="foot-menu" style="margin-top:7px"><li>Sub Menu</li><li>Sub menu</li><li>Sub Menu</li><li>Sub Menu</li><li>Sub Menu</li><li>Sub Menu</li></ul>
    </div>
    <div class="abs" style="left:218px;top:78px">
      <h3 class="foot-head">MENU 2</h3>
      <ul class="foot-menu" style="margin-top:7px"><li>Sub Menu</li><li>Sub menu</li><li>Sub Menu</li><li>Sub Menu</li><li>Sub Menu</li><li>Sub Menu</li></ul>
    </div>
    <div class="abs" style="left:345px;top:78px">
      <h3 class="foot-head">MENU 3</h3>
      <ul class="foot-menu" style="margin-top:7px"><li>Sub Menu</li><li>Sub menu</li><li>Sub Menu</li><li>Sub Menu</li><li>Sub Menu</li><li>Sub Menu</li></ul>
    </div>
    <div class="abs social" style="left:0;top:0;width:1029px;height:265px">
      <h3 class="abs foot-head" style="left:540px;top:66px">CONNECT</h3>
      <span style="left:527px" aria-label="Social profile 1"></span>
      <span style="left:553px" aria-label="Social profile 2"></span>
      <span style="left:580px" aria-label="Social profile 3"></span>
      <span style="left:607px" aria-label="Social profile 4"></span>
      <span style="left:634px" aria-label="Social profile 5"></span>
    </div>
    <div class="abs" style="left:725px;top:63px;width:240px;text-align:center">
      <h3 class="foot-head">OWEN HALVORSEN</h3>
      <address class="contact-info" style="font-style:normal;margin-top:6px">
        Die Schreibstube<br>Lindenweg 42b<br>10115 Berlin<br>Germany<br>Telephone: +49 30 55512345<br>E-mail: hallo@owenhalvorsen-demo.de
      </address>
    </div>
  </footer>
</div>
</body>
</html>
```